Indian Takeaway Menu

We need a flyer for an existing Indian Takeaway business in dublin Ireland.

We need some upto date style menu may be a A4 sheet folded in 3 layers.

But not folded in landscape side folded from portrait side and typing from portrait side from top, as we type in a word document and then fold the letter in 3 layers.
please amend your designs as everyone have done the same thing which is very boring.

We have a logo we would like to use in front of the menu. Designer have to come up with the colour which will help the logo to stand out. we also have a review in the paper which we would like to use at the back page somewhere.

New ideas are welcome from the designer
Please look at the example menu attached.

City population

Landscape

Font styles to use
Sans Serif

Colors
acd037

Requirements
Must have
• ingredient sign for
• Nuts
• Celiac
• Low fat
• Diary
Nice to have
• attractive

```html
<!DOCTYPE html>
<html lang="en">
<head>
<meta charset="utf-8">
<title>Takeaway Menu – Inside Spread</title>
<link href="https://fonts.googleapis.com/css2?family=Aladin&family=Alegreya+Sans+SC:wght@500&family=Kalam:wght@300&display=swap" rel="stylesheet">
<style>
:root{
  --paper:#f3dd95;
  --paper-light:#f8ebb8;
  --paper-dark:#e3c46f;
  --ink:#1c140a;
  --ink-soft:#3a2b16;
  --chilli:#d3261b;
  --chilli-stem:#3d7a1f;
  --lowfat:#8cc63f;
  --dairy:#2f6fb5;
  --nut:#c0392b;
  --biryani:#c7661e;
  --emblem:#3b2d1c;
}
*{margin:0;padding:0;box-sizing:border-box}
html,body{width:1200px;height:849px;overflow:hidden}
body{
  background:
    radial-gradient(ellipse at 30% 40%, var(--paper-light) 0%, transparent 55%),
    radial-gradient(ellipse at 80% 70%, var(--paper-light) 0%, transparent 50%),
    radial-gradient(ellipse at 50% 50%, var(--paper) 40%, var(--paper-dark) 100%);
  color:var(--ink);
  position:relative;
}
.column{position:absolute;top:0}
.col-1{left:30px;width:374px}
.col-2{left:425px;width:346px}
.col-3{left:796px;width:370px}
.section{position:absolute;left:0;right:0}
.section-title{
  font-family:"Aladin",cursive;font-size:15px;font-weight:400;letter-spacing:.3px;
  display:flex;align-items:flex-end;gap:6px;line-height:18px;margin-bottom:4px;color:var(--ink);
}
.emblem{display:inline-block;width:32px;height:26px;border-radius:40% 45% 30% 30%;background:var(--emblem);opacity:.85}
.item{margin-bottom:5px}
.item.roomy{margin-bottom:7px}
.item-row{display:flex;justify-content:space-between;align-items:center;height:17px}
.name{font-family:"Alegreya Sans SC",sans-serif;font-weight:500;font-size:12px;color:var(--ink);display:flex;align-items:center;gap:6px}
.price{font-family:"Alegreya Sans SC",sans-serif;font-weight:500;font-size:12px;color:var(--ink)}
.desc{font-family:"Kalam",cursive;font-weight:300;font-style:italic;font-size:10.5px;line-height:14px;color:var(--ink-soft)}
.icon{display:inline-block;vertical-align:middle}
.lowfat{width:20px;height:20px;border-radius:50%;background:var(--lowfat)}
.dairy{width:11px;height:18px}
.bowl{width:20px;height:10px;border-radius:50%;background:var(--biryani)}
.chilli{width:20px;height:12px}
.no-nuts{width:20px;height:20px}
</style>
</head>
<body>

<!-- Column one -->
<div class="column col-1">
  <section class="section" style="top:34px">
    <h2 class="section-title">Vegetarian Starters <span class="emblem" role="img" aria-label="Elephant emblem"></span></h2>
    <div style="margin-left:4px;margin-top:6px">
      <div class="item"><div class="item-row"><span class="name">Onion Bhajia</span><span class="price">€4.00</span></div>
        <p class="desc">Sliced onions, fresh spinach and herbs fried with gram flour until golden.</p></div>
      <div class="item"><div class="item-row"><span class="name">Vegetable Samosa</span><span class="price">€4.00</span></div>
        <p class="desc">Crispy handmade pastry filled with potato and peas deep fried with herb until golden.</p></div>
      <div class="item"><div class="item-row"><span class="name">Palak Kachori</span><span class="price">€4.00</span></div>
        <p class="desc">Golden fried cakes of fresh spinach and yellow chana lentil, served with tamarind dip. (Recommended)</p></div>
      <div class="item"><div class="item-row"><span class="name">Veg Pakora</span><span class="price">€4.00</span></div>
        <p class="desc">Cauliflower, potato and onion golden fried with gram flour batter.</p></div>
      <div class="item"><div class="item-row"><span class="name">Aloo Channa chat <span class="icon lowfat" role="img" aria-label="Low fat"></span></span><span class="price">€3.50</span></div>
        <p class="desc">Aloo channa chaat is a low fat snack made with boiled chickpeas, potatoes and chaat masala</p></div>
    </div>
  </section>

  <section class="section" style="top:340px">
    <h2 class="section-title">Vegetarian Dishes <span class="emblem" role="img" aria-label="Elephant emblem"></span></h2>
    <div style="margin-top:10px">
      <div class="item roomy"><div class="item-row"><span class="name">Gajjar Mattar Paneer
        <svg class="icon chilli" viewBox="0 0 20 12" role="img" aria-label="Spicy"><path d="M2 4 Q9 11 18 6 Q10 8 4 2Z" fill="var(--chilli)"/><path d="M2 4 L1 1" stroke="var(--chilli-stem)" stroke-width="1.5"/></svg>
        <svg class="icon dairy" viewBox="0 0 11 18" role="img" aria-label="Dairy"><rect x="1" y="3" width="9" height="14" rx="2" fill="#fff" stroke="var(--dairy)"/><rect x="3" y="0.5" width="5" height="3" fill="var(--dairy)"/></svg></span><span class="price">€8.00</span></div>
        <p class="desc">Mildly spicy. A colour combination of chopped carrots, peas and Indian cheese in a semi-dry sauce. A recommended chef's special for vegetarians.</p></div>
      <div class="item roomy"><div class="item-row"><span class="name">Dhingri Dulma
        <svg class="icon chilli" viewBox="0 0 20 12" role="img" aria-label="Spicy"><path d="M2 4 Q9 11 18 6 Q10 8 4 2Z" fill="var(--chilli)"/><path d="M2 4 L1 1" stroke="var(--chilli-stem)" stroke-width="1.5"/></svg></span><span class="price">€8.00</span></div>
        <p class="desc">Mildly spicy. Fresh mushrooms and Indian cheese fried with onions, ginger and garlic in mild spices.</p></div>
      <div class="item roomy"><div class="item-row"><span class="name">Dum Wale Aloo</span><span class="price">€7.70</span></div>
        <p class="desc">Potatoes cooked with fresh ginger, garlic, onions, tomatoes, curry leaves &amp; slow cooked with cumin flavoured yoghurt.</p></div>
      <div class="item"><div class="item-row"><span class="name">Karahi Paneer
        <svg class="icon dairy" viewBox="0 0 11 18" role="img" aria-label="Dairy"><rect x="1" y="3" width="9" height="14" rx="2" fill="#fff" stroke="var(--dairy)"/><rect x="3" y="0.5" width="5" height="3" fill="var(--dairy)"/></svg></span><span class="price">€7.70</span></div>
        <p class="desc">A semi-dry and colourful curry prepared using homemade Indian cheese.</p></div>
      <div class="item roomy"><div class="item-row"><span class="name">Paneer Jalfrezi
        <svg class="icon dairy" viewBox="0 0 11 18" role="img" aria-label="Dairy"><rect x="1" y="3" width="9" height="14" rx="2" fill="#fff" stroke="var(--dairy)"/><rect x="3" y="0.5" width="5" height="3" fill="var(--dairy)"/></svg></span><span class="price">€8.00</span></div>
        <p class="desc">Stir-fried homemade cottage cheese &amp; peppers with roasted coriander seeds, fresh tomatoes, onions and green chillies</p></div>
      <div class="item roomy"><div class="item-row"><span class="name">Sambhar Vegetable Curry</span><span class="price">€7.70</span></div>
        <p class="desc">Mixed seasonal vegetable curry cooked with a lentils, coconut, curry leaves, mustard seeds and fresh coriander (recommended)</p></div>
      <div class="item"><div class="item-row"><span class="name">Aloo Saag Hariyali</span><span class="price">€7.70</span></div>
        <p class="desc">Pan fried potatoes &amp; spinach, flavoured with kasoori methi and fresh coriander</p></div>
      <div class="item"><div class="item-row"><span class="name">Vegetable Biryani <span class="icon bowl" role="img" aria-label="Biryani"></span></span><span class="price">€8.50</span></div>
        <p class="desc">Basmati rice cooked with mixed seasonal vegetables, fresh herbs, spices and fried golden onions. Served with your choice of vegetables or raita.</p></div>
    </div>
  </section>
</div>

<!-- Column two -->
<div class="column col-2">
  <section class="section" style="top:26px">
    <h2 class="section-title">Meat Starters <span class="emblem" role="img" aria-label="Elephant emblem"></span></h2>
    <div class="item"><div class="item-row"><span class="name">Keema Singhara</span><span class="price">€4.00</span></div>
      <p class="desc">Crispy handmade pastry filled with lamb mince,fresh herbs and spices accompanied with a tongue tingling mint chutney</p></div>
    <div class="item"><div class="item-row"><span class="name">Prawn Chatpate</span><span class="price">€5.00</span></div>
      <p class="desc">Pan-fried prawns cooked with tangy lemon and coriander sauce</p></div>
    <div class="item"><div class="item-row"><span class="name">Chicken Tikka</span><span class="price">€4.50</span></div>
      <p class="desc">Tender pieces of chicken marinated, cooked in a clay oven and served with salad and a Mint dip.</p></div>
    <div class="item"><div class="item-row"><span class="name">Seekh Kebab</span><span class="price">€5.00</span></div>
      <p class="desc">A lamb mince barbecued delicacy, served with salad and a mint dip</p></div>
    <div class="item"><div class="item-row"><span class="name">Chicken Pakora</span><span class="price">€ 5.00</span></div>
      <p class="desc">Boneless pieces of chicken coated in batter/spice, deep fried.</p></div>
  </section>

  <section class="section" style="top:286px">
    <h2 class="section-title" style="line-height:22px;width:330px">Clay Oven Dishes Served with Nan<br>&amp; Curry Sauce <span class="emblem" role="img" aria-label="Elephant emblem" style="margin-left:auto;margin-right:10px;margin-bottom:10px"></span></h2>
    <div style="margin-top:8px">
      <div class="item"><div class="item-row"><span class="name">Tandoori Chicken (Half)</span><span class="price">€ 9.50</span></div>
        <p class="desc">Spring chicken marinated with yoghurt and tandoori spices, grilled in clay oven</p></div>
      <div class="item"><div class="item-row"><span class="name">Chicken Tikka</span><span class="price">€9.50</span></div>
        <p class="desc">Tender breast pieces of chicken marinated and cooked in a clay oven</p></div>
      <div class="item"><div class="item-row"><span class="name">Seekh Kebab</span><span class="price">€10.00</span></div>
        <p class="desc">A lamb mince barbecued delicacy</p></div>
      <div class="item"><div class="item-row"><span class="name">Saffron Hearth's Mix Grill</span><span class="price">€10.50</span></div>
        <p class="desc">2 pcs of chicken tikka, 2 pcs seekh kebab, 2 pcs battered prawns, 1 pc tandoori chicken</p></div>
      <div class="item"><div class="item-row"><span class="name">***Chicken Dansak <span class="icon lowfat" role="img" aria-label="Low fat"></span></span><span class="price">€8.50</span></div>
        <p class="desc">Sweet and sour sauce prepared with mixed fruit and spices.</p></div>
      <div class="item"><div class="item-row"><span class="name">Chicken Saag</span><span class="price">€9.50</span></div>
        <p class="desc">Chicken breast pieces cooked with spinach , fresh herbs, tomato tangy sauce and coriander</p></div>
      <div class="item"><div class="item-row"><span class="name">Chicken Royale Korma</span><span class="price">€8.50</span></div>
        <p class="desc">Chopped breast of chicken cooked in a rich creamy sauce with coconut , probably most popular amongst the Irish</p></div>
      <div class="item"><div class="item-row"><span class="name">Saffron Hearth Chicken Curry</span><span class="price">€8.50</span></div>
        <p class="desc">Traditional Indian chicken curry to suit most palates—mild, medium or hot, you choose.</p></div>
      <div class="item"><div class="item-row"><span class="name">Chicken Karahi
        <svg class="icon chilli" viewBox="0 0 20 12" role="img" aria-label="Spicy"><path d="M2 4 Q9 11 18 6 Q10 8 4 2Z" fill="var(--chilli)"/><path d="M2 4 L1 1" stroke="var(--chilli-stem)" stroke-width="1.5"/></svg></span><span class="price">€8.00</span></div>
        <p class="desc">Diced chicken prepared with green peppers, spring onions, tomatoes and whole Indian spices.</p></div>
      <div class="item"><div class="item-row"><span class="name">Chicken Tikka Masala</span><span class="price" style="margin-right:26px">€8.00</span></div>
        <p class="desc">Tender chicken tikka cooked in a smooth creamy tomato sauce,<br>Most popular</p></div>
    </div>
  </section>
</div>

<!-- Column three -->
<div class="column col-3">
  <section class="section" style="top:27px">
    <div class="item"><div class="item-row"><span class="name">South-Indian Garlic Chilli
      <svg class="icon chilli" viewBox="0 0 20 12" role="img" aria-label="Spicy"><path d="M2 4 Q9 11 18 6 Q10 8 4 2Z" fill="var(--chilli)"/><path d="M2 4 L1 1" stroke="var(--chilli-stem)" stroke-width="1.5"/></svg></span><span class="price">€8.00</span></div>
      <p class="desc">Tasty red chicken curry loaded with garlic, ground spices, fresh herbs and green chillies.</p></div>
    <div class="item"><div class="item-row"><span class="name">Chicken dahiwala
      <svg class="icon chilli" viewBox="0 0 20 12" role="img" aria-label="Spicy"><path d="M2 4 Q9 11 18 6 Q10 8 4 2Z" fill="var(--chilli)"/><path d="M2 4 L1 1" stroke="var(--chilli-stem)" stroke-width="1.5"/></svg></span><span class="price">€8.00</span></div>
      <p class="desc">Amazingly spicy chicken curry with fresh coconut, yoghurt, green chillies, ginger and herbs.</p></div>
    <div class="item"><div class="item-row"><span class="name">Chicken Vegetable &amp; Nut Curry
      <svg class="icon chilli" viewBox="0 0 20 12" role="img" aria-label="Spicy"><path d="M2 4 Q9 11 18 6 Q10 8 4 2Z" fill="var(--chilli)"/><path d="M2 4 L1 1" stroke="var(--chilli-stem)" stroke-width="1.5"/></svg></span><span class="price">€8.50</span></div>
      <p class="desc">Boneless chicken breast pieces sautéed with fresh vegetables, nuts and herbs in a smooth and creamy sauce.</p></div>
    <div class="item"><div class="item-row"><span class="name">Chicken Biryani <span class="icon bowl" role="img" aria-label="Biryani"></span></span><span class="price">€ 9.00</span></div>
      <p class="desc">Breast of chicken chopped and cooked with Basmati rice, fresh herbs, spices and fried onions accompanied with vegetable curry.</p></div>
  </section>

  <section class="section" style="top:232px">
    <h2 class="section-title">Lamb Dishes <span class="emblem" role="img" aria-label="Elephant emblem"></span></h2>
    <div class="item"><div class="item-row"><span class="name">Lamb Bhuna</span><span class="price">€ 9.50</span></div>
      <p class="desc">Spring lamb pieces sautéed with spring onions, tomatoes, crushed black pepper and fresh herbs</p></div>
    <div class="item"><div class="item-row"><span class="name">Haandi Gosht</span><span class="price">€ 9.50</span></div>
      <p class="desc">Lamb cooked with chunky pepper, onions, tomatoes, mushrooms, green chilli and fresh coriander</p></div>
    <div class="item"><div class="item-row"><span class="name">Palak Gosht</span><span class="price">€9.50</span></div>
      <p class="desc">Pan-fried lamb pieces cooked with spinach, fresh herbs and coriander</p></div>
    <div class="item"><div class="item-row"><span class="name">Lamb Roganjosh
      <svg class="icon chilli" viewBox="0 0 20 12" role="img" aria-label="Spicy"><path d="M2 4 Q9 11 18 6 Q10 8 4 2Z" fill="var(--chilli)"/><path d="M2 4 L1 1" stroke="var(--chilli-stem)" stroke-width="1.5"/></svg></span><span class="price">€ 9.50</span></div>
      <p class="desc">A red lamb curry prepared with fresh herbs and spices, a delicacy from Kashmir.</p></div>
    <div class="item"><div class="item-row"><span class="name">Lamb Kohlapuri
      <svg class="icon chilli" viewBox="0 0 20 12" role="img" aria-label="Spicy"><path d="M2 4 Q9 11 18 6 Q10 8 4 2Z" fill="var(--chilli)"/><path d="M2 4 L1 1" stroke="var(--chilli-stem)" stroke-width="1.5"/></svg></span><span class="price">€10.00</span></div>
      <p class="desc">A hot lamb dish from the southern coast of India, flavoured with yoghurt and coconut. Kashmir.</p></div>
    <div class="item"><div class="item-row"><span class="name">Lamb Jalfrezi
      <svg class="icon no-nuts" viewBox="0 0 20 20" role="img" aria-label="Contains nuts"><circle cx="10" cy="10" r="8.5" fill="none" stroke="var(--nut)" stroke-width="1.6"/><line x1="4" y1="4" x2="16" y2="16" stroke="var(--nut)" stroke-width="1.6"/></svg></span><span class="price">€10.00</span></div>
      <p class="desc">A semi-dry dish of lamb, tossed with strips of onions, assorted bell peppers, tomatoes and flavoured with crushed coriander seeds and dry fenugreek.</p></div>
    <div class="item"><div class="item-row"><span class="name">Gosht Biryani Sofyani</span><span class="price">€10.50</span></div>
      <p class="desc">Basmati rice cooked with cubed Irish lamb flavoured with fresh mint and fried onion. Accompanied with vegetable curry.</p></div>
  </section>

  <section class="section" style="top:603px">
    <h2 class="section-title">Seafood Dishes <span class="emblem" role="img" aria-label="Elephant emblem"></span></h2>
    <div class="item"><div class="item-row"><span class="name">Tandoori Prawn Masala</span><span class="price">€10.00</span></div>
      <p class="desc">Sautéed prawns in a smooth creamy sauce flavoured with kasoori methi and tandoori spices</p></div>
    <div class="item"><div class="item-row"><span class="name">Prawn Karahi
      <svg class="icon chilli" viewBox="0 0 20 12" role="img" aria-label="Spicy"><path d="M2 4 Q9 11 18 6 Q10 8 4 2Z" fill="var(--chilli)"/><path d="M2 4 L1 1" stroke="var(--chilli-stem)" stroke-width="1.5"/></svg></span><span class="price">€10.00</span></div>
      <p class="desc">Succulent prawns cooked with green peppers, spring onions, tomatoes &amp; whole spices</p></div>
    <div class="item"><div class="item-row"><span class="name">Goan Prawn Curry
      <svg class="icon chilli" viewBox="0 0 20 12" role="img" aria-label="Spicy"><path d="M2 4 Q9 11 18 6 Q10 8 4 2Z" fill="var(--chilli)"/><path d="M2 4 L1 1" stroke="var(--chilli-stem)" stroke-width="1.5"/></svg></span><span class="price">€10.50</span></div>
      <p class="desc">Fisherman's favourite prawn curry flavoured with curry leaves, coconut, crushed spices &amp; fresh herbs</p></div>
    <div class="item"><div class="item-row"><span class="name">Prawn Biryani
      <svg class="icon chilli" viewBox="0 0 20 12" role="img" aria-label="Spicy"><path d="M2 4 Q9 11 18 6 Q10 8 4 2Z" fill="var(--chilli)"/><path d="M2 4 L1 1" stroke="var(--chilli-stem)" stroke-width="1.5"/></svg></span><span class="price">€10.00</span></div>
      <p class="desc">Shrimp prawn cooked with eggs, green peas and onion.</p></div>
  </section>
</div>

</body>
</html>
```